Innovative WordPress for a non-profit organization dedicated to providing healthcare to the less for

Bright Harbor Aid is a small non-profit organization. BHA's core mission is to provide free medical and dental care to the less fortunate. Aside from providing healthcare, BHA also helps build infrastructure such as orphanage, cancer centers, water wells and small homes for the homeless. As a non-profit, BHA has been sponsoring various social programs to help those in need. From building infrastructure to health care and most recently micro-finance, the BHA team is helping to GIve Back to the community at person at a time.

BHA is growing and needs help to restructure for the future. The corporate website design is the first step in a new branding strategy for the company.

BHA current website is divided into three specific target areas:
1. Mission: This area is dedicated to provide information about medical and dental mission hosted by BHA.

2. Infrastructure. This area is dedicated to provide information about infrastructure programs supported and completed by the BHA team. The projects includes orphanage, cancer centers. water wells, micro-finance, small homes for the homeless...etc.

3. Special Projects. This area is used to showcase specific short term projects which might come up.

Aside from the specific three target area, BHA also needs a NEWS area where news about BHA can be published.

Please put your thinking cape on and help produce the next generation WordPress template for Bright Harbor Aid. Your design will great enhance the level of volunteers recruited and also increase the level of help that BHA can provide for other.

For a quick glance at the BHA website today, please visit http://www.bhaexample.org. The BHA team is looking for a fresh design.

Thank you very much for taking the time to help BHA advance its mission of helping those in need.

Reason: Seeking more variety in design. Design needs to have a donate button, sponsors area, news, welcome message, 3 primary functions (mission, infrastructure, and specials projects). The BHA logo is available. Please note, you have the option to NOT use the colors associated with BHA logo. Thank you for helping with designing the new site.

Non-Profit

Requirements
Must have
• 1. Donate Now button.
2. Primary focus areas: MISSION / INFRASTRUCTURE / SPECIAL PROJECTS
3. News & Events
4. Welcome Message area
5. Sponsors area - place to add sponsor logos

Nice to have
• 1. Photo of the Month: Used to show a specific photo to represent events or functions completed by the BHA team.

Please show sample of one level down. For example, what does the page look like when I click the MISSION link.

```html
<!DOCTYPE html>
<html lang="en">
<head>
<meta charset="utf-8">
<title>Bright Harbor Aid – Serving The Disadvantage Community</title>
<link href="https://fonts.googleapis.com/css2?family=Arimo:wght@400;700&display=swap" rel="stylesheet">
<style>
:root{
  --red:#e3141b;
  --red-dark:#a90c10;
  --green:#0c9a45;
  --ink:#222;
  --text:#333;
  --darker:#262626;
  --footer:#4a4a4a;
  --panel:#f2f2f2;
  --line:#d6d6d6;
  --sponsor:#8a8a8a;
}
*{box-sizing:border-box;margin:0;padding:0}
html,body{width:960px;height:1200px;overflow:hidden}
body{position:relative;font-family:"Arimo",Arial,sans-serif;color:var(--text);background:#ebebeb}
.abs{position:absolute}
.backdrop{position:absolute;left:0;top:0}

/* header */
.header{left:0;top:0;width:960px;height:126px;background:linear-gradient(#fff,#f1f1f1 70%,#dcdcdc)}
.tagline{left:138px;top:44px;width:250px;text-align:center;font-size:21px;line-height:21px;color:#444}
.logo-tab{left:388px;top:14px;width:184px;height:134px}
.logo-name{left:388px;top:58px;width:184px;text-align:center;font-size:30px;font-weight:700;color:var(--ink);letter-spacing:1px}
.logo-sub{left:388px;top:94px;width:184px;text-align:center;font-size:10px;font-weight:700;color:var(--ink)}
.search-input{left:584px;top:53px;width:156px;height:20px;background:#fff;border:1px solid #bbb}
.search-btn{left:746px;top:53px;width:70px;height:20px;background:var(--green);color:#fff;font-size:12px;text-align:center;line-height:20px}
.donate-btn{left:706px;top:82px;width:110px;height:24px;background:var(--red);color:#fff;font-size:12px;font-weight:700;text-align:center;line-height:24px;border-radius:2px}

/* footer band sits behind the sheet */
.footer{left:0;top:1046px;width:960px;height:154px;background:var(--footer)}

/* main sheet */
.sheet{left:130px;top:130px;width:700px;height:928px;background:#fff;box-shadow:0 0 6px rgba(0,0,0,.35)}
.nav-ribbon{left:116px;top:134px;width:728px;height:40px}
.nav{left:133px;top:136px;width:694px;height:31px;display:flex;list-style:none}
.nav li{flex:1;color:#fff;font-size:13px;text-align:center;line-height:31px;border-right:1px solid rgba(0,0,0,.18)}
.nav li:last-child{border-right:0}

.slide{left:133px;top:170px;width:694px;height:282px;background:linear-gradient(120deg,#2c4f86 0%,#6b5a4c 40%,#9b7b62 55%,#2c4f86 85%)}
.slide-arrow{top:282px;width:26px;height:50px;background:rgba(0,0,0,.75);color:#fff;font-size:22px;text-align:center;line-height:50px}
.slide-title{left:133px;top:356px;width:694px;text-align:center;color:#fff;font-size:19px;font-weight:700;line-height:20px;text-shadow:0 1px 3px #000}
.slide-sub{left:133px;top:406px;width:694px;text-align:center;color:#fff;font-size:12px;text-shadow:0 1px 2px #000}

.dots-ribbon{left:343px;top:457px;width:274px;height:48px}
.dot{top:470px;width:10px;height:10px;border-radius:50%;background:#fff}
.dot.on{background:var(--green)}

/* focus cards */
.card{top:516px;width:222px;height:182px;background:linear-gradient(#fff,#efefef);border:1px solid #cfcfcf;box-shadow:0 1px 4px rgba(0,0,0,.25)}
.card h2{position:absolute;left:0;top:6px;width:100%;text-align:center;font-size:17px;font-weight:400;color:var(--ink)}
.card .photo{position:absolute;left:12px;top:29px;width:197px;height:73px}
.card p{position:absolute;left:12px;top:108px;width:200px;font-size:9px;line-height:11px;color:#444}
.card .btn{position:absolute;left:78px;top:156px;width:66px;height:16px;font-size:9px;line-height:16px}
.btn{background:var(--green);color:#fff;text-align:center;border-radius:2px}

/* welcome */
.welcome-title{left:150px;top:726px;font-size:18px;font-weight:400;color:var(--ink)}
.welcome-title span{color:var(--red)}
.welcome-text{left:150px;top:760px;width:430px;font-size:9.6px;line-height:13px;color:#333}
.welcome-text p+p{margin-top:13px}
.welcome-btn{left:499px;top:911px;width:66px;height:17px;font-size:9px;line-height:17px}

.testimonials{left:140px;top:938px;width:440px;height:113px;background:var(--panel);border:1px solid var(--line)}
.testimonials h3{position:absolute;left:10px;top:6px;font-size:13px;font-weight:400;color:var(--ink)}
.testimonials .portrait{position:absolute;left:22px;top:30px;width:70px;height:70px;border:2px solid #fff;box-shadow:0 0 2px #999}
.quote-mark{position:absolute;color:var(--red);font-size:26px;font-weight:700;line-height:26px}
.testimonials blockquote{position:absolute;left:114px;top:34px;width:305px;font-size:9.6px;line-height:12px;color:#333}
.testimonials cite{position:absolute;left:114px;top:84px;font-style:normal;font-size:9.6px;color:#333}
.testimonials .pager{position:absolute;left:408px;top:89px;font-size:14px;font-weight:700;color:#222}

/* news */
.news{left:594px;top:716px;width:226px;height:336px;background:#fff;border:1px solid var(--line)}
.news h3{position:absolute;left:8px;top:7px;font-size:12.5px;font-weight:400;color:var(--ink)}
.news .rule{position:absolute;left:0;top:28px;width:100%;height:3px;background:#ddd}
.news-item{position:absolute;left:0;width:100%;height:61px;background:#f4f4f4;border-bottom:1px solid #fff}
.news-item .thumb{position:absolute;left:10px;top:11px;width:42px;height:42px;border:2px solid #fff;box-shadow:0 0 2px #aaa}
.news-item b{position:absolute;left:68px;top:12px;font-size:7.6px;color:#222}
.news-item time{position:absolute;left:68px;top:22px;font-size:7.6px;color:#555}
.news-item p{position:absolute;left:68px;top:32px;width:148px;font-size:7.6px;line-height:9px;color:#555}
.news .view-all{position:absolute;right:8px;top:312px;font-size:10.5px;color:var(--red);text-decoration:underline}

/* footer content */
.footer-nav{left:130px;top:1066px;width:700px;height:28px;background:var(--darker);display:flex;list-style:none}
.footer-nav li{flex:1;color:#fff;font-size:11.5px;text-align:center;line-height:28px}
.follow{left:170px;top:1106px;width:120px;text-align:center;font-size:10.5px;color:#fff}
.social{top:1122px;width:18px;height:18px;border-radius:2px;background:#7d8c9e}
.sponsors-label{left:150px;top:1156px;font-size:10px;color:#fff;line-height:16px}
.sponsor{top:1156px;width:36px;height:16px;border-radius:2px;background:var(--sponsor)}
.foot-logo{left:440px;top:1108px;width:80px;text-align:center}
.foot-logo .sq{display:block;margin:0 auto 4px;width:20px;height:20px;background:var(--green)}
.foot-logo b{font-size:17px;font-weight:700;color:#222}
.newsletter-title{left:617px;top:1099px;font-size:12px;color:#f2c200}
.newsletter-text{left:617px;top:1116px;width:206px;text-align:center;font-size:11px;line-height:12px;color:#fff}
.nl-input{left:624px;top:1146px;width:140px;height:17px;background:#fff;font-size:8px;color:#555;line-height:17px;padding-left:6px}
.nl-btn{left:770px;top:1146px;width:50px;height:17px;font-size:9.5px;font-weight:700;line-height:17px}
.copyright{left:0;top:1180px;width:960px;height:20px;background:#111;color:#fff;font-size:10px;text-align:center;line-height:20px}
</style>
</head>
<body>

<svg class="backdrop" width="960" height="1200" aria-hidden="true">
  <defs>
    <linearGradient id="darkBand" x1="0" y1="0" x2="0" y2="1">
      <stop offset="0" stop-color="#4d4d4d"/><stop offset="1" stop-color="#2f2f2f"/>
    </linearGradient>
  </defs>
  <rect width="960" height="1200" fill="#ececec"/>
  <path d="M0 120 H960 V470 Q700 380 420 395 Q170 410 0 440 Z" fill="url(#darkBand)"/>
  <path d="M0 440 Q170 410 420 395 Q700 380 960 470 V520 Q700 430 420 440 Q170 450 0 480 Z" fill="#fff" opacity=".55"/>
</svg>

<header>
  <div class="abs header"></div>
  <div class="abs tagline">Serving The Disadvantage Community</div>
  <svg class="abs logo-tab" viewBox="0 0 184 134" aria-hidden="true">
    <path d="M0 0 H184 Q170 8 166 30 V96 Q160 124 92 134 Q24 124 18 96 V30 Q14 8 0 0 Z" fill="#f7f7f7" stroke="#b9b9b9" stroke-width="2"/>
  </svg>
  <div class="abs logo-name">BHA</div>
  <div class="abs logo-sub">BRIGHT HARBOR AID</div>
  <div class="abs search-input"></div>
  <div class="abs search-btn">Search</div>
  <div class="abs donate-btn">Donate Now</div>
</header>

<div class="abs footer"></div>

<main>
  <div class="abs sheet"></div>

  <svg class="abs nav-ribbon" viewBox="0 0 728 40" aria-hidden="true">
    <path d="M0 6 H20 V34 H0 L8 20 Z" fill="var(--red-dark)"/>
    <path d="M728 6 H708 V34 H728 L720 20 Z" fill="var(--red-dark)"/>
    <rect x="14" y="2" width="700" height="31" fill="var(--red)"/>
  </svg>
  <ul class="abs nav">
    <li>Home</li><li>About Us</li><li>Mission</li><li>Special Projects</li><li>Infrastructure</li><li>Events</li>
  </ul>

  <div class="abs slide" role="img" aria-label="Photo of two dentists examining a patient at a free dental clinic"></div>
  <div class="abs slide-arrow" style="left:133px">‹</div>
  <div class="abs slide-arrow" style="left:801px">›</div>
  <div class="abs slide-title">Dr. Linh Tran and Dr. Bao Vo at a BHA hosted<br>free Dental Clinic</div>
  <div class="abs slide-sub">Dr. Tran and Dr. Vo conferring about patient and determining what treatments to give</div>

  <svg class="abs dots-ribbon" viewBox="0 0 274 48" aria-hidden="true">
    <path d="M0 16 H40 V40 H0 L12 28 Z" fill="var(--red-dark)"/>
    <path d="M274 16 H234 V40 H274 L262 28 Z" fill="var(--red-dark)"/>
    <rect x="30" y="2" width="214" height="34" fill="var(--red)"/>
  </svg>
  <span class="abs dot on" style="left:445px"></span>
  <span class="abs dot" style="left:459px"></span>
  <span class="abs dot" style="left:473px"></span>
  <span class="abs dot" style="left:487px"></span>
  <span class="abs dot" style="left:501px"></span>

  <section class="abs card" style="left:150px">
    <h2>MISSION</h2>
    <div class="photo" role="img" aria-label="Group photo of volunteers at a medical mission" style="background:linear-gradient(#7c8a6a,#c9b79a)"></div>
    <p>Through the years, bright harbor aid has hosted numerous different type of dental/ medical missions. Most recently, the BHA team hosted a free dental clinic at the ...</p>
    <div class="btn">Read more</div>
  </section>
  <section class="abs card" style="left:374px">
    <h2>INFRASTRUCTURE</h2>
    <div class="photo" role="img" aria-label="Photo of a cancer center building" style="background:linear-gradient(#9fb3c9,#c58a6a 60%,#6f7a5a)"></div>
    <p>May Lotus Bay Cancer Center - gay HouseASide from hosting various dental and medical missions through out the year, the BHA team also engages in infrastructure ...</p>
    <div class="btn">Read more</div>
  </section>
  <section class="abs card" style="left:598px">
    <h2>SPECIAL PROJECTS</h2>
    <div class="photo" role="img" aria-label="Photo of a volunteer team in green shirts outdoors" style="background:linear-gradient(#5f8f4a,#a6d24c 60%,#6d7d4a)"></div>
    <p>Through the years, bright harbor aid has hosted numerous different type of dental/ medical missions. Most recently, the BHA team hosted a free dental clinic at the ...</p>
    <div class="btn">Read more</div>
  </section>

  <h1 class="abs welcome-title">Welcome To <span>BrightHarbor.com</span></h1>
  <div class="abs welcome-text">
    <p>Bright Harbor Aid (BHA) is non profit - 501 C (3) organization dedicated to providing health-care, Human services, and educational assistance to underprivelleged communities. we work in collaboration with various groups and non-governmental organizations (NGOs), to delivers humanitarian goods, services and relief to improverished regions. The team is comprised of professionals with a broadspectrum of experiences. the combined mission trips of our team span across north America, South Africa, South America, and South East Asia, bringing a variety of general and specialized disciplines to each region.</p>
    <p>The BHA team initial medical mission project was Phnom Penh, Cambodia in March 2005. The mission team provided care to over 2.500 patients. in november 2005, The BHA Team..</p>
  </div>
  <div class="abs btn welcome-btn">read more</div>

  <section class="abs testimonials">
    <h3>Testimonials</h3>
    <div class="portrait" role="img" aria-label="Portrait photo of the person giving the testimonial" style="background:linear-gradient(#e9d6c4,#b98a6a)"></div>
    <span class="quote-mark" style="left:96px;top:28px">“</span>
    <blockquote>Lorem ipsum dolor sit amet, consecteteur adipiscing wlit. Sed diem nonumy inconvalis gravida neque. Nulla gravida vestibulum metis a acumsan, aliquam in sagittis ut.</blockquote>
    <span class="quote-mark" style="left:280px;top:58px">”</span>
    <cite>Mira Sato, Phnom Penh</cite>
    <span class="pager">‹ ›</span>
  </section>

  <aside class="abs news">
    <h3>Latest News &amp; Events</h3>
    <div class="rule"></div>
    <div class="news-item" style="top:34px">
      <div class="thumb" role="img" aria-label="News photo of a medical worker" style="background:linear-gradient(#dfe8f0,#6f93b8)"></div>
      <b>Lorem ipsum dolor sit amet</b><time>March, 22th 2014</time>
      <p>Lorem ipsum dolor sit amet,consecteteur adipiscing elit. set diem nonumy...</p>
    </div>
    <div class="news-item" style="top:96px">
      <div class="thumb" role="img" aria-label="News photo of a clinic visit" style="background:linear-gradient(#e6eef4,#8fb2cf)"></div>
      <b>Lorem ipsum dolor sit amet</b><time>March, 22th 2014</time>
      <p>Lorem ipsum dolor sit amet,consecteteur adipiscing elit. set diem nonumy...</p>
    </div>
    <div class="news-item" style="top:158px">
      <div class="thumb" role="img" aria-label="News photo of a smiling patient" style="background:linear-gradient(#f1dccb,#c07f5a)"></div>
      <b>Lorem ipsum dolor sit amet</b><time>March, 22th 2014</time>
      <p>Lorem ipsum dolor sit amet,consecteteur adipiscing elit. set diem nonumy...</p>
    </div>
    <div class="news-item" style="top:220px">
      <div class="thumb" role="img" aria-label="News photo of healthy food" style="background:linear-gradient(#f2e4b0,#8cb04a)"></div>
      <b>Lorem ipsum dolor sit amet</b><time>March, 22th 2014</time>
      <p>Lorem ipsum dolor sit amet,consecteteur adipiscing elit. set diem nonumy...</p>
    </div>
    <span class="view-all">View All</span>
  </aside>
</main>

<footer>
  <ul class="abs footer-nav">
    <li>Home</li><li>About Us</li><li>Mission</li><li>Special Projects</li><li>Infrastructure</li><li>Events</li>
  </ul>
  <div class="abs follow">FOLLOW US ON :</div>
  <span class="abs social" style="left:166px"></span>
  <span class="abs social" style="left:188px"></span>
  <span class="abs social" style="left:210px"></span>
  <span class="abs social" style="left:232px"></span>
  <span class="abs social" style="left:254px"></span>
  <span class="abs social" style="left:276px"></span>
  <div class="abs sponsors-label">SPONSORS :</div>
  <span class="abs sponsor" style="left:216px"></span>
  <span class="abs sponsor" style="left:258px"></span>
  <span class="abs sponsor" style="left:300px"></span>
  <span class="abs sponsor" style="left:342px"></span>
  <div class="abs foot-logo"><span class="sq"></span><b>BHA</b></div>
  <div class="abs newsletter-title">Newsletter</div>
  <div class="abs newsletter-text">Sign Up and start receive our<br>newsletter weekly</div>
  <div class="abs nl-input">Your email address</div>
  <div class="abs btn nl-btn">SUBMIT</div>
  <div class="abs copyright">Copyright © 2014, BrightHarbor.com. All rights reserved.</div>
</footer>

</body>
</html>
```